Coastal Heritage Dairywrights' Guild needs new business cards

We need new business cards designed and produced. We are likely to need other design work done for ads, flyers etc in future.

We would like to start with an initial business card.

The Coastal Heritage Dairywrights' Guild (CHDG) is a membership-based not-for-profit organisation that looks after the interests of Australia's small to medium artisan cheesemakers, many of whom are also small-scale farmers. The design should be simple, using our logo, but also communicate our artisan cheese and small dairy farm focus.

The first card to be designed and produced is for me, Megan Thorburn. My details are:

Megan Thorburn
Secretary
Coastal Heritage Dairywrights' Guild (CHDG)
http://www.curdandcrockery.org
T +61427583914
E megan.meganthorburn@mailfern.net

I have attached the CHDG logo in jpg form. I have a higher resolution version available if needed.

Thank you!

Megan

Business

Megan Thorburn
Coastal Heritage Dairywrights' Guild
megan.meganthorburn@mailfern.net
+61427583914

Sans Serif

• Logo (see attached file)

```html
<!DOCTYPE html>
<html lang="en">
<head>
<meta charset="utf-8">
<title>CHDG Business Card</title>
<link rel="stylesheet" href="https://fonts.googleapis.com/css2?family=Open+Sans:wght@400;600;700&display=swap">
<style>
  :root {
    --bg: #3a2418;
    --card: #ffffff;
    --brown: #4a3222;
    --cheese: #fdcc6c;
    --accent: #f7bf55;
    --shadow: rgba(0, 0, 0, 0.35);
  }
  * { box-sizing: border-box; margin: 0; padding: 0; }
  html, body { width: 1200px; height: 1000px; overflow: hidden; }
  body {
    background: var(--bg);
    font-family: "Open Sans", Arial, sans-serif;
    color: var(--brown);
    position: relative;
  }
  .card {
    position: absolute;
    background: var(--card);
    border-radius: 18px;
    overflow: hidden;
    box-shadow: 0 6px 18px var(--shadow);
  }
  /* Front */
  .card-front { left: 330px; top: 160px; width: 560px; height: 310px; }
  .front-mark {
    position: absolute; left: 48px; top: 100px;
    display: flex; align-items: center; gap: 12px;
  }
  .mark-dot { width: 46px; height: 46px; border-radius: 50%; background: var(--cheese); }
  .mark-name { font-size: 26px; font-weight: 600; color: var(--brown); }
  .divider {
    position: absolute; left: 225px; top: 70px;
    width: 2px; height: 170px; background: var(--brown);
  }
  .details { position: absolute; left: 255px; top: 72px; }
  .org { font-size: 14px; line-height: 1.15; }
  .person { margin-top: 12px; font-size: 23px; font-weight: 700; line-height: 1.1; }
  .person .surname { color: var(--accent); font-weight: 600; }
  .role { font-size: 17px; margin-top: 2px; }
  .contact { margin-top: 16px; font-size: 14px; line-height: 1.2; }
  /* Back */
  .card-back { left: 418px; top: 510px; width: 515px; height: 295px; }
  .cheese-art { position: absolute; right: 0; top: 0; width: 250px; height: 250px; }
  .back-mark {
    position: absolute; left: 32px; top: 160px;
    display: flex; align-items: center; gap: 14px;
  }
  .back-mark .mark-dot { width: 56px; height: 56px; }
  .back-name { font-size: 19px; line-height: 1.2; color: var(--brown); font-weight: 400; }
</style>
</head>
<body>
  <section class="card card-front">
    <div class="front-mark">
      <span class="mark-dot"></span>
      <span class="mark-name">CHDG</span>
    </div>
    <div class="divider"></div>
    <div class="details">
      <p class="org">Coastal Heritage<br>Dairywrights' Guild (CHDG)</p>
      <p class="person">Megan <span class="surname">Thorburn</span></p>
      <p class="role">Secretary</p>
      <p class="contact">+61 42 75 83 914<br>www.curdandcrockery.org<br>megan.meganthorburn@mailfern.net</p>
    </div>
  </section>

  <section class="card card-back">
    <svg class="cheese-art" viewBox="0 0 250 250" role="img" aria-label="Large cheese wedge illustration with holes">
      <path d="M0 0 H250 V245 H185 Q160 240 140 230 Q60 200 25 130 Q0 70 0 0 Z" fill="var(--cheese)"/>
    </svg>
    <div class="back-mark">
      <span class="mark-dot"></span>
      <p class="back-name">Coastal Heritage<br>Dairywrights'<br>Guild</p>
    </div>
  </section>
</body>
</html>
```